依頼詳細
そこを通れば見落とさずに、入ってこれるような、目立つ看板で、それなりにカッコいいけど親しみやすい雰囲気がいいです。
サイズは縦長で、縦360cm×横90cmです。
記載項目
タイドオービット、Tide Orbit、株式会社アウルリード、Owl-Reed
希望イメージ
シンプル 複雑
単色 カラフル
暗い 明るい
日常 高級
遊び心 厳粛
未来的 伝統的
女性的 男性的
希望する色
赤系、緑系、黄・オレンジ系
納品ファイル
• 高解像度JPG (.jpg)
• イラストレーター形式 (.ai)
• フォトショップ形式 (.psd)
補足説明
イメージカラーは明るい緑とオレンジです。
会社のロゴは添付の通りなので、そのOwl-Reedの部分を、Tide Orbit/タイドオービットにして、その下に「Produced by Owl-Reed Inc」というように入れて使ってもらいたいです。
ロゴを添付します

```html
<!DOCTYPE html>
<html lang="ja">
<head>
<meta charset="utf-8">
<title>Tide Orbit — Vertical Signboard</title>
<link rel="stylesheet" href="https://fonts.googleapis.com/css2?family=Poppins:wght@500;600;700&family=M+PLUS+1p:wght@500;700&display=swap">
<style>
  :root {
    --orange: #ee8d2d;
    --orange-deep: #e07020;
    --green: #3da54a;
    --green-deep: #1f6b34;
    --brown: #7a4a24;
    --charcoal: #333333;
    --white: #ffffff;
    --black: #0c0c0c;
  }
  html, body {
    margin: 0;
    padding: 0;
    width: 1200px;
    height: 4792px;
    overflow: hidden;
    background: var(--black);
  }
  .signboard {
    position: relative;
    width: 1200px;
    height: 4792px;
    overflow: hidden;
  }
  .hero {
    position: absolute;
    left: 0;
    top: 0;
    width: 1200px;
    height: 3780px;
  }
  .hero svg { display: block; }
  .title-latin {
    font-family: "Poppins", sans-serif;
    font-weight: 600;
  }
  .title-kana {
    font-family: "M PLUS 1p", sans-serif;
    font-weight: 700;
  }
  .producer-line {
    font-family: "Poppins", sans-serif;
    font-weight: 500;
  }
  .footer-band {
    position: absolute;
    left: 0;
    top: 3780px;
    width: 1200px;
    height: 1012px;
    background: var(--black);
    display: flex;
    flex-direction: column;
    align-items: center;
  }
  .brand-mark {
    width: 230px;
    height: 230px;
    margin-top: 110px;
    border-radius: 50%;
    background: var(--orange);
  }
  .brand-name {
    margin-top: 110px;
    font-family: "Poppins", sans-serif;
    font-weight: 600;
    font-size: 168px;
    line-height: 1;
    color: var(--white);
    letter-spacing: 2px;
    white-space: nowrap;
  }
  .brand-kana {
    margin-top: 28px;
    font-family: "M PLUS 1p", sans-serif;
    font-weight: 700;
    font-size: 76px;
    line-height: 1;
    color: var(--white);
    letter-spacing: 6px;
  }
  .brand-producer {
    margin-top: 38px;
    font-family: "Poppins", sans-serif;
    font-weight: 600;
    font-size: 46px;
    line-height: 1;
    color: var(--white);
  }
</style>
</head>
<body>
<main class="signboard">
  <section class="hero">
    <svg width="1200" height="3780" viewBox="0 0 1200 3780" xmlns="http://www.w3.org/2000/svg">
      <defs>
        <radialGradient id="honeycomb-tone" cx="0.55" cy="0.5" r="0.7">
          <stop offset="0" stop-color="#7a4a24" stop-opacity="0"/>
          <stop offset="0.7" stop-color="#7a4a24" stop-opacity="0.12"/>
          <stop offset="1" stop-color="#1f6b34" stop-opacity="0.25"/>
        </radialGradient>
      </defs>
      <rect class="hero-green" x="0" y="0" width="1200" height="3780" fill="var(--green)"/>
      <ellipse class="hero-orange" cx="960" cy="1750" rx="940" ry="2250" fill="var(--orange)"/>
      <rect class="honeycomb-area" x="0" y="0" width="1200" height="3780" fill="url(#honeycomb-tone)" role="img" aria-label="Scattered hexagon honeycomb pattern in brown, dark green and deep orange"/>

      <text class="title-latin" transform="translate(610 60) rotate(90)" font-size="500" textLength="3560" lengthAdjust="spacingAndGlyphs">
        <tspan fill="var(--white)">Tide </tspan><tspan fill="var(--charcoal)">Orbit</tspan>
      </text>

      <text class="title-kana" transform="translate(355 300) rotate(90)" font-size="112" fill="var(--white)" textLength="1180" lengthAdjust="spacingAndGlyphs">タイドオービット</text>

      <text class="producer-line" transform="translate(415 1580) rotate(90)" font-size="104" fill="var(--white)" textLength="2080" lengthAdjust="spacingAndGlyphs">Produced by Owl-Reed Inc</text>
    </svg>
  </section>

  <footer class="footer-band">
    <div class="brand-mark"></div>
    <div class="brand-name">Tide Orbit</div>
    <div class="brand-kana">タイドオービット</div>
    <div class="brand-producer">Produced by Owl-Reed Inc</div>
  </footer>
</main>
</body>
</html>
```